Flyer Design for a Boston Therapeutic Clinic

I am a body therapist who needs a couple of flyers designed:
1. To fit half a page.
2. To fit a 5 inch by 3.5 inch flyer.
My practice is based in Boston, MA and my web site is:
www.LarkfieldTane.Com
For the First half page:
A. Have my company's name and color shown as it appears on my web site (Larkfield Tane)
B. Have the following text: "Control your weight (This part should be emphasized) by balancing your nervous and digestive system through the Tane Method. The Tane Method, a technique developed by Dr. Wenna. Tane, uses physical pressure to manipulate visceral tissue to bring back resiliency and proper functioning of the whole body."
Also helps with
-Constipation
-Bloating
-IBS
-eating disorders and overeating
Our practitioner is highly experienced. Please visit our web sites for reviews.
C. I would like to have a nice earthy feeling, something that feels "freeing" like open flowers, or an open land scape such as mountains or fields.
D. I also like the color blue, white, orange; perhaps if these colors can be integrated into the flyer, that would be great.
E. "Visit our web site LarkfieldTane.com or call 413-908-2617"
The Smaller Flyer :
A.The smaller Flyer should also have my Company's name as shown on my web site (Larkfield Tane)
B.The following text: " Restore your body's natural resiliency and greatly reduce your physical pain through the Dr. Wenna Tane Method of Structural Integration."
C. "Our practitioner is highly experienced and has a great reputation; visit our web site for reviews."
"Benefits:
"reduce aches and pains
reduce joint pain
reduce chronic muscular tension"
D, "feel better after the first session!"
E. if you could use a picture of me working on someone from my web site, that would be great.
F. I also like the colors white, orange and silver, for this one.
G. "Visit our web site LarkfieldTane.com or call 413-908 2617"
I am very open minded,
I would like the flyer to evoke a sense of tranquility, professionalism, and simplicity. So if you have another angle you think would look good, then go for it! As long as it looks clean, professional and helpful.
Thanks a lot!
If you need any pictures from my web site, I have the original high resolution files that i can send.
Professionals and working men and women from ages 20-70
Clinic

```html
<!DOCTYPE html>
<html lang="en">
<head>
<meta charset="utf-8">
<title>Larkfield Tane Therapy – Flyer</title>
<link rel="stylesheet" href="https://fonts.googleapis.com/css2?family=Josefin+Slab:wght@400;600&family=Alegreya:wght@500&family=Signika:wght@500&family=Arimo:ital,wght@0,400;1,400&display=swap">
<style>
  :root {
    --orange: #f07a2b;
    --orange-deep: #e4661a;
    --ink: #2f2a33;
    --paper: #f1f1ef;
    --skin-light: #e8c3a6;
    --skin-mid: #d39a74;
    --skin-deep: #a9683f;
    --white: #ffffff;
  }
  * { box-sizing: border-box; margin: 0; padding: 0; }
  html, body { width: 1200px; height: 856px; overflow: hidden; background: var(--paper); }
  .flyer {
    position: relative;
    width: 1200px;
    height: 856px;
    overflow: hidden;
    background: var(--paper);
  }
  .hero-photo {
    position: absolute;
    top: 0; right: 0;
    width: 760px; height: 856px;
    background:
      radial-gradient(ellipse 40% 30% at 70% 35%, rgba(255,225,200,.55), transparent 70%),
      radial-gradient(ellipse 45% 35% at 80% 75%, rgba(150,90,55,.45), transparent 70%),
      linear-gradient(160deg, var(--skin-light) 0%, var(--skin-mid) 50%, var(--skin-deep) 100%);
    -webkit-mask-image: linear-gradient(90deg, transparent 0%, rgba(0,0,0,.35) 25%, #000 55%);
    mask-image: linear-gradient(90deg, transparent 0%, rgba(0,0,0,.35) 25%, #000 55%);
  }
  .brand-title {
    position: absolute;
    left: 73px; top: 108px;
    font-family: "Josefin Slab", serif;
    font-weight: 400;
    font-size: 64px;
    letter-spacing: 1px;
    color: var(--ink);
    white-space: nowrap;
  }
  .brand-title .brand-name { color: var(--orange); }
  .intro {
    position: absolute;
    left: 73px; top: 248px;
    width: 820px;
    font-family: "Alegreya", serif;
    font-weight: 500;
    font-size: 30px;
    line-height: 50px;
    color: var(--ink);
  }
  .session-photo {
    position: absolute;
    left: 73px; top: 443px;
    width: 336px; height: 321px;
    border: 8px solid var(--orange);
    border-radius: 30px;
    background:
      radial-gradient(ellipse 50% 40% at 40% 70%, rgba(240,200,150,.8), transparent 70%),
      linear-gradient(150deg, #b98460 0%, #e0b48e 45%, #c98a5c 100%);
  }
  .benefits {
    position: absolute;
    left: 473px; top: 484px;
    color: var(--ink);
  }
  .benefits-label {
    font-family: "Arimo", sans-serif;
    font-style: italic;
    font-size: 28px;
    letter-spacing: 3px;
    margin-bottom: 16px;
  }
  .benefits-list {
    list-style: none;
    font-family: "Signika", sans-serif;
    font-weight: 500;
    font-size: 31px;
    line-height: 45px;
  }
  .benefits-list li::before {
    content: "";
    display: inline-block;
    width: 9px; height: 9px;
    border-radius: 50%;
    background: var(--orange);
    margin: 0 10px 6px 0;
    vertical-align: middle;
  }
  .reputation-note {
    position: absolute;
    left: 428px; top: 708px;
    width: 560px;
    font-family: "Arimo", sans-serif;
    font-style: italic;
    font-size: 20px;
    line-height: 30px;
    color: var(--ink);
  }
  .contact-band {
    position: absolute;
    left: 1041px; top: 0;
    width: 107px; height: 713px;
    background: var(--orange);
    border-radius: 0 0 24px 24px;
  }
  .contact-text {
    position: absolute;
    left: 50%; top: 50%;
    width: 690px;
    transform: translate(-50%, -50%) rotate(-90deg);
    font-family: "Arimo", sans-serif;
    font-size: 33px;
    line-height: 40px;
    letter-spacing: 1px;
    color: var(--white);
    text-align: center;
    white-space: nowrap;
  }
</style>
</head>
<body>
  <main class="flyer">
    <div class="hero-photo" role="img" aria-label="Close-up photo of a therapist's hands pressing into a client's bare back"></div>

    <h1 class="brand-title"><span class="brand-name">Larkfield</span> Tane Therapy</h1>

    <p class="intro">Restore your body's natural resiliency and<br>greatly reduce your physical pain through the<br>Dr. Wenna Tane Method of Structural Integration.</p>

    <div class="session-photo" role="img" aria-label="Photo of a client lying relaxed while the therapist works on her shoulders"></div>

    <section class="benefits">
      <h2 class="benefits-label">Benefits:</h2>
      <ul class="benefits-list">
        <li>reduce aches and pains</li>
        <li>reduce joint pain</li>
        <li>reduce chronic muscular tension</li>
      </ul>
    </section>

    <p class="reputation-note">Our practitioner is highly experienced and has a great reputation; visit our web site for reviews.</p>

    <aside class="contact-band">
      <p class="contact-text">Visit our web site LarkfieldTane.com<br>or call 413-908 2617</p>
    </aside>
  </main>
</body>
</html>
```